we need a design for Water Bottle Lable Wrap
The product is called Corvane Water is a restructured water. its a very healthy and rejuvenating water
we were looking at using as a tag ling Restore, Recover, Rejuvenate.

```html
<!DOCTYPE html>
<html lang="en">
<head>
<meta charset="utf-8">
<title>Corvane Water – Bottle Label Wrap</title>
<link rel="stylesheet" href="https://fonts.googleapis.com/css2?family=Josefin+Sans:wght@400;600&display=swap">
<style>
  :root {
    --page-bg: #e4e4e4;
    --label-deep: #0c1d2c;
    --label-mid: #163a55;
    --label-glow: #2f6f93;
    --ice-light: #a9d9ee;
    --ice-mid: #4f9cc4;
    --ice-deep: #1a4d72;
    --name-blue: #9fdcf2;
    --tagline-white: #f2f7fa;
  }

  html, body {
    margin: 0;
    padding: 0;
  }

  body {
    width: 1200px;
    height: 3036px;
    overflow: hidden;
    background: var(--page-bg);
    position: relative;
  }

  .label-wrap {
    position: absolute;
    left: 60px;
    top: 518px;
    width: 1080px;
    height: 2000px;
    overflow: hidden;
  }

  .label-backdrop {
    position: absolute;
    inset: 0;
    background:
      radial-gradient(ellipse 70% 35% at 55% 52%, var(--label-glow) 0%, rgba(47,111,147,0) 70%),
      linear-gradient(180deg, var(--label-deep) 0%, var(--label-mid) 45%, #10283d 70%, var(--label-deep) 100%);
  }

  .ice-photo {
    position: absolute;
    left: 0;
    right: 0;
    bottom: 0;
    height: 820px;
    background:
      radial-gradient(ellipse 60% 45% at 35% 45%, var(--ice-light) 0%, rgba(169,217,238,0) 70%),
      radial-gradient(ellipse 50% 40% at 80% 55%, var(--ice-mid) 0%, rgba(79,156,196,0) 75%),
      linear-gradient(180deg, rgba(26,77,114,0) 0%, var(--ice-deep) 30%, #12395a 100%);
  }

  .brand-name {
    position: absolute;
    left: 0;
    right: 0;
    top: 220px;
    margin: 0;
    text-align: center;
    font-family: "Josefin Sans", sans-serif;
    font-weight: 400;
    font-size: 196px;
    line-height: 210px;
    letter-spacing: 4px;
    text-transform: uppercase;
    color: var(--name-blue);
  }

  .brand-name span {
    display: block;
  }

  .tagline {
    position: absolute;
    left: 0;
    right: 0;
    top: 690px;
    margin: 0;
    text-align: center;
    font-family: "Josefin Sans", sans-serif;
    font-weight: 600;
    font-size: 54px;
    letter-spacing: 1px;
    text-transform: uppercase;
    color: var(--tagline-white);
  }

  .tagline .dot {
    display: inline-block;
    margin: 0 14px;
  }
</style>
</head>
<body>
  <section class="label-wrap">
    <div class="label-backdrop" role="img" aria-label="Dark blue water texture with rising bubbles"></div>
    <div class="ice-photo" role="img" aria-label="Pile of clear ice cubes lit in cool blue light"></div>

    <h1 class="brand-name"><span>Corvane</span><span>Water</span></h1>

    <p class="tagline">Restore<span class="dot">•</span>Recover<span class="dot">•</span>Rejuvenate</p>
  </section>
</body>
</html>
```